Affiliate website design and wireframe

We need a design of an affiliate website for an application we purchased, it is important that you build the website pages according to the developer of the applications specifications (please see attached documents) the developer of the application will configure the pages and add them to the site. Please take special note of his comments below.

We all so need you to create a wire frame so the developer can test everything (http://sketchwire.tolvaro.vn/)

It will be the homepage and about 16 inner pages (please see attached files)
Here is our website http://bluvendmarket.com/affiliate/affiliates/index.php

The version of the software we purchased is the Kivo Partner Hubline version

Comments from the developers

1. I will need the source files of the design (photoshop .psd files and font files if custom fonts are used), since the implementation is closely bound to component sizes (like border width, margin width etc.) and colors. If you own a corporate design manual, it's crucial to send it as well. Also, please, make sure if you use custom fonts, that these allow legal website integration (like google web fonts).

2. Any and every content is controlled via templates. All editing/adding/removing etc. is done here. The template files are essentially html/php documents, they use a template engine called quillo (http://www.quillo.net/) which has it's own language similar to php.

3. .psd files are ideal, because we deal with the specifics of KPX/KPH implementation on a daily basis. Any html/css developed in advance may prove to be a poor choice. You may choose to let an in-house developer do the job, but experience wise this is more costly, since he will not be accustomed to the template/functionality systems of KPX/KPH.

4. I will need the source files of the design (photoshop .psd files and font files if custom fonts are used), since the implementation is closely bound to component sizes (like border width, margin width etc.) and colors. If you own a corporate design manual, it's crucial to send it as well. Also, please, make sure if you use custom fonts, that these allow legal website integration (like google web fonts).

Regards,

Dorek Hanval
Multimedia Design

We prefer illustrations more than pictures of real people.

This is the home page, it is asking for Merchant and Affiliate sign up, not just affiliate.

http://bluvendmarket.com/affiliate/index.php

Please note the home page features both Merchant and Affiliate sign up

We are looking for illustration design not just stock images

Please remember the search menu that searches for the available programs, see the example we gave you, look at the search menu at the top of the page http://www.tradelumo.com/

We are reviewing everything, no need to send more designs

Target Market(s)

Natural Products Manufacturers
Natural products Sales reps
Natural Products Bloggers
Social Marketing

Industry/Entity Type

Software

Requirements
Must have
• 1. All links on pages should go to the appropriate pages.
2. Colors can be based on our logo design (look at the attachments)
3. Here is our website http://bluvendmarket.com/affiliate/affiliates/index.php
4. We have attached a drawing of how we think the homepage concept should follow.
5. Main concept of design, is trying to show our sales people (Affiliates) are doing multiple things to advertise and sell the merchants products.(see logo)
6. Need to be able to edit all text and images.
7. Our target audience is Natural product sales people (Advertisers, bloggers, ext) and natural product manufacturers.
8. You can speak to the company who made the application, through live chat, on there website http://www.kivopartnerhubline.com/
Nice to have
• See Attached Documents.
site should take up whole website pages
Look For fun Illustrated Website, one of the better ones we have seen is http://www.tradelumo.com/index.cfm
Should not have
• Please look very carefully at developers comment above.

```html
<!DOCTYPE html>
<html lang="en">
<head>
<meta charset="utf-8">
<title>BluvendMarket – Affiliate Home</title>
<link href="https://fonts.googleapis.com/css2?family=Open+Sans:wght@400;600;700&family=PT+Sans:wght@400;700&family=Fjalla+One&display=swap" rel="stylesheet">
<style>
:root{
  --band:#c6d0dc;
  --navy:#1d3c6e;
  --btn:#2c3e55;
  --ink:#333b46;
  --muted:#555;
  --link:#2e5e9c;
  --green:#5aa51e;
  --red:#e8402a;
  --rule:#e2e6ea;
  --hero-dark:#2a1a12;
  --hero-mid:#5a3a26;
  --footer:#f2f2f2;
}
*{margin:0;padding:0;box-sizing:border-box}
html,body{width:1200px;height:1000px;overflow:hidden;background:#fff}
body{position:relative;font-family:"Open Sans",Arial,sans-serif;color:var(--ink)}
.abs{position:absolute}
.page{position:absolute;left:314px;top:0;width:572px;height:1000px}

.topbar{left:314px;top:0;width:572px;height:14px;background:var(--band);font-size:7px;color:#334}
.topbar .item{position:absolute;top:3px;display:flex;align-items:center;gap:5px}
.sq{display:inline-block;width:6px;height:8px}

.brand{left:395px;top:30px;display:flex;align-items:center;gap:4px;font-family:"PT Sans",sans-serif;font-weight:700;font-size:12px;color:var(--green)}
.brand .dot{width:12px;height:12px;border-radius:50%;background:var(--navy)}
.nav{top:46px;font-size:7px;color:var(--navy)}

.hero{left:314px;top:60px;width:572px;height:221px;background:radial-gradient(ellipse at 50% 60%,#8a5a30 0%,var(--hero-mid) 40%,var(--hero-dark) 100%)}
.hero-tag{left:573px;top:70px;width:215px;height:34px;background:rgba(40,25,18,.75);color:#f0ece6;font-size:10px;display:flex;align-items:center;justify-content:center}
.hero-bar{left:435px;top:250px;width:333px;height:25px;border:1px solid rgba(255,255,255,.35);background:rgba(255,255,255,.12);display:flex;align-items:center;color:#fff;font-size:8.5px}
.hero-bar span{flex:1;text-align:center;display:flex;align-items:center;justify-content:center;gap:4px}
.hero-bar .sep{flex:0 0 1px;height:12px;background:rgba(255,255,255,.6)}

.welcome h1{left:392px;top:296px;font-family:"PT Sans",sans-serif;font-size:15px;font-weight:700;color:#1a1a1a;white-space:nowrap}
.welcome h1 em{font-style:normal;color:var(--green)}
.welcome .sub{left:392px;top:316px;font-size:8px;color:#333}
.welcome .body{left:392px;top:339px;width:235px;font-size:5.6px;line-height:1.75;color:#444}
.proposal{left:651px;top:300px;width:155px;height:19px;background:var(--navy);color:#fff;font-family:"Fjalla One",sans-serif;font-size:8px;display:flex;align-items:center;justify-content:center}
.callnum{left:690px;top:333px;font-size:12px;color:var(--red)}
.callnote{left:658px;top:358px;font-family:"PT Sans",sans-serif;font-size:9px;color:#333}

.band{left:314px;top:390px;width:572px;height:123px;background:var(--band)}
.card{left:392px;top:400px;width:414px;height:103px;background:#fff}
.card h2{position:absolute;top:5px;width:100%;text-align:center;font-weight:400;font-size:9.5px;line-height:1.25;color:var(--navy)}
.card p{position:absolute;top:33px;left:60px;width:294px;text-align:center;font-size:5.8px;line-height:1.9;color:#333}
.card p a{color:var(--link);text-decoration:none}
.card .split{position:absolute;top:53px;left:0;width:100%;height:1px;background:var(--rule)}
.card .vsplit{position:absolute;top:53px;left:206px;width:1px;height:50px;background:var(--rule)}
.login{position:absolute;top:58px;width:207px;text-align:center;font-size:8.5px;color:var(--navy)}
.login .btn{display:block;margin:5px auto 0;width:88px;height:20px;background:var(--btn);color:#fff;font-size:6.5px;line-height:20px;box-shadow:0 1px 2px rgba(0,0,0,.3)}

.sec-title{left:392px;width:414px;text-align:center;font-size:9.5px;color:var(--navy);line-height:1.25}
.sec-title::before,.sec-title::after{content:"";position:absolute;top:6px;height:1px;background:var(--rule);width:100px}
.sec-title::before{left:0}.sec-title::after{right:0}

.timeline{left:350px;top:639px;width:496px;height:1px;background:var(--rule)}
.channel{position:absolute;width:80px;margin-left:-40px;text-align:center;font-size:9px;color:var(--navy)}

.tools{left:392px;top:730px;width:414px;height:92px;display:flex}
.tool{flex:1;position:relative;text-align:center;border-right:1px solid var(--rule);padding:0 4px}
.tool:last-child{border-right:none}
.tool h3{font-weight:400;font-size:8px;color:#222;margin-top:3px}
.tool p{margin-top:13px;font-size:5.6px;line-height:1.55;color:#333}
.tool .more{position:absolute;right:0;bottom:0;font-size:5.6px;color:var(--navy)}

.hr{left:392px;width:414px;height:1px;background:var(--rule)}
.col h4{font-weight:400;font-size:8.5px;color:var(--navy)}
.col .box{margin-top:5px;width:112px;height:50px;background:#f1f1f1;border-left:3px solid #c9d2df;padding:5px 6px;font-size:4.6px;line-height:1.6;color:#333}
.subscribe input{display:block;margin-top:5px;width:78px;height:12px;border:1px solid #b9c4d3;font-size:4.6px;padding-left:3px;font-family:inherit;color:#888}
.subscribe .go{position:absolute;left:88px;top:33px;width:13px;height:13px;background:#d6e4f3;border:1px solid #9bb;color:var(--link);font-size:8px;text-align:center;line-height:11px}

.footnav{top:953px;font-size:6.5px;color:var(--link)}
.bottombar{left:314px;top:980px;width:572px;height:13px;background:var(--footer);font-size:5.8px;color:#444}
.bottombar a{color:var(--link);text-decoration:none}
</style>
</head>
<body>

<!-- Top utility bar -->
<div class="abs topbar">
  <div class="item" style="left:264px">
    <svg width="8" height="6" viewBox="0 0 8 6"><rect x=".5" y=".5" width="7" height="5" fill="#2c3e55"/><path d="M.5 .5 4 3.5 7.5 .5" stroke="#c6d0dc" fill="none" stroke-width=".8"/></svg>
    support@bluvendmarket.com
  </div>
  <div class="item" style="left:398px">
    <svg width="6" height="7" viewBox="0 0 6 7"><path d="M1 .5h1.5l.6 1.6-.9.7a4 4 0 0 0 1.6 1.8l.7-.9 1.5.6V6a1 1 0 0 1-1 .6A5 5 0 0 1 .4 1.4 1 1 0 0 1 1 .5z" fill="#2c3e55"/></svg>
    +1800 004477
  </div>
  <div class="item" style="left:464px;top:2px;gap:3px">
    <span class="sq" style="background:#3b5998"></span>
    <span class="sq" style="background:#d8412f"></span>
    <span class="sq" style="background:#4fb6e8"></span>
  </div>
</div>

<!-- Header -->
<div class="abs brand"><span class="dot"></span>BluvendMarket</div>
<div class="abs nav" style="left:579px">Home</div>
<div class="abs nav" style="left:612px">About us</div>
<div class="abs nav" style="left:655px">Merchants ▾</div>
<div class="abs nav" style="left:708px">Signup</div>
<div class="abs nav" style="left:743px">Blog</div>
<div class="abs nav" style="left:768px">Contact us</div>

<!-- Hero -->
<div class="abs hero" role="img" aria-label="Photo of green coffee juice bottles with pineapple, bananas, cherries, apples, mango and blueberries on a dark wooden table"></div>
<div class="abs hero-tag">Earn up to 50% commission for all products!</div>
<div class="abs hero-bar">
  <span>Affiliate <svg width="9" height="9" viewBox="0 0 10 10"><circle cx="5" cy="5" r="4.3" fill="none" stroke="#fff"/><path d="M3 5h4M5.2 3.2 7 5 5.2 6.8" stroke="#fff" fill="none"/></svg></span>
  <i class="sep"></i>
  <span>Sign up</span>
  <i class="sep"></i>
  <span>Merchant <svg width="9" height="9" viewBox="0 0 10 10"><circle cx="5" cy="5" r="4.3" fill="none" stroke="#fff"/><path d="M3 5h4M5.2 3.2 7 5 5.2 6.8" stroke="#fff" fill="none"/></svg></span>
</div>

<!-- Welcome -->
<div class="welcome">
  <h1 class="abs">Welcome To <em>BluvendMarket</em></h1>
  <div class="abs sub">Bluvendmarket is a Lorem Ipsum is simply dummy text</div>
  <p class="abs body">Lorem Ipsum is simply dummy text of the printing and typesetting industry. Lorem Ipsum has been the industry's standard dummy text ever since the 1500s, when an of type and scrambled it to make a type specimen book...</p>
</div>
<div class="abs proposal">Request Free Affiliate Marketing Proposal</div>
<div class="abs callnum">1800-004477</div>
<div class="abs callnote">Call Us now for more Information</div>

<!-- Login band -->
<div class="abs band"></div>
<div class="abs card">
  <h2>Let's Create your Company's<br>Affiliate Marketing Strategy Together</h2>
  <p>Lorem Ipsum is simply dummy text of the <a href="#">printing and typesetting</a> industry. Lorem Ipsum has been the industry's standard</p>
  <div class="split"></div><div class="vsplit"></div>
  <div class="login" style="left:0">Merchants Login<span class="btn">Click here Merchants</span></div>
  <div class="login" style="left:207px">Affiliate Login<span class="btn">Click here Affiliates</span></div>
</div>

<!-- Channels -->
<div class="abs sec-title" style="top:531px">Connect with us and Earn Money up to 50%<br>For every products!</div>
<div class="abs timeline"></div>
<svg class="abs" style="left:350px;top:585px" width="500" height="60" viewBox="350 585 500 60">
  <g fill="none" stroke-width="1.2">
    <circle cx="413" cy="607" r="17" stroke="#7cc6e6"/><circle cx="411" cy="606" r="14" fill="#7cc6e6" stroke="none"/>
    <circle cx="512" cy="607" r="17" stroke="#e2c27a"/><circle cx="510" cy="606" r="14" fill="#e2c27a" stroke="none"/>
    <circle cx="605" cy="607" r="17" stroke="#7fd6a8"/><circle cx="603" cy="606" r="14" fill="#7fd6a8" stroke="none"/>
    <circle cx="695" cy="607" r="17" stroke="#8aa7e6"/><circle cx="693" cy="606" r="14" fill="#8aa7e6" stroke="none"/>
    <circle cx="788" cy="607" r="17" stroke="#b890e0"/><circle cx="786" cy="606" r="14" fill="#b890e0" stroke="none"/>
  </g>
  <g fill="none" stroke="#fff" stroke-width="1.6" stroke-linecap="round" stroke-linejoin="round">
    <path d="M405 612l2-6 8-8 4 4-8 8z"/>
    <rect x="503" y="600" width="13" height="13" rx="1"/><path d="M508 608l9-9M512 599h5v5"/>
    <path d="M596 603h14l-2 9h-10z"/><path d="M600 603v9M603 603v9M606 603v9M599 603l3-5M607 603l-3-5"/>
    <rect x="685" y="599" width="16" height="11" rx="1"/><path d="M693 610v3M689 613h8M688 607l3-3 2 2 4-4"/>
    <circle cx="786" cy="606" r="7"/><path d="M783 609v-2M786 609v-4M789 609v-6"/>
  </g>
  <g><circle cx="415" cy="640" r="2.5" fill="#7cc6e6"/><circle cx="512" cy="640" r="2.5" fill="#e2c27a"/><circle cx="605" cy="640" r="2.5" fill="#7fd6a8"/><circle cx="696" cy="640" r="2.5" fill="#8aa7e6"/><circle cx="789" cy="640" r="2.5" fill="#b890e0"/></g>
</svg>
<div class="channel" style="left:414px;top:656px">E-mail</div>
<div class="channel" style="left:512px;top:656px">Content</div>
<div class="channel" style="left:605px;top:656px">Blog</div>
<div class="channel" style="left:696px;top:656px">Social Network</div>
<div class="channel" style="left:789px;top:656px">SEO</div>

<!-- Tools -->
<div class="abs sec-title" style="top:701px">Use Tools &amp; Make Money</div>
<div class="abs tools">
  <div class="tool"><h3>Merchant Ads</h3><p>Lorem Ipsum is simply dummy text of printing and typesetting tha industry. Lorem Ipsum has been the industry's standard dummy.</p><span class="more">Learn more &gt;&gt;</span></div>
  <div class="tool"><h3>Paid Placement</h3><p>Lorem Ipsum is simply dummy text of printing and typesetting tha industry. Lorem Ipsum has been the industry's standard dummy.</p><span class="more">Learn more &gt;&gt;</span></div>
  <div class="tool"><h3>Custom Link Builder</h3><p>Lorem Ipsum is simply dummy text of printing and typesetting tha industry. Lorem Ipsum has been the industry's standard dummy.</p><span class="more">Learn more &gt;&gt;</span></div>
  <div class="tool"><h3>Dynamic Deal</h3><p>Lorem Ipsum is simply dummy text of printing and typesetting tha industry. Lorem Ipsum has been the industry's standard dummy.</p><span class="more">Learn more &gt;&gt;</span></div>
</div>
<div class="abs hr" style="top:833px"></div>

<!-- News / testimonials / subscribe -->
<div class="abs col" style="left:400px;top:847px"><h4>What's News</h4><div class="box">Lorem Ipsum :- Lorem Ipsum is simply dummy text of printing and typesetting industry. Lorem Ipsum has been the industry's standard.</div></div>
<div class="abs col" style="left:542px;top:847px"><h4>Our Customers Speak</h4><div class="box">" Lorem Ipsum is simply dummy text of printing and typesetting industry. Lorem Ipsum has been the industry's standard dummy text ever since the but also the leap into electronic "</div></div>
<div class="abs col subscribe" style="left:685px;top:847px"><h4>Subscribe</h4><div class="box" style="position:relative">Lorem Ipsum is simply dummy text of printing and typesetting industry. Lorem Ipsum has been the industry's standard<input type="text" value="Your Email ID"><span class="go">+</span></div></div>

<!-- Footer -->
<div class="abs hr" style="top:939px"></div>
<div class="abs footnav" style="left:425px">Home</div>
<div class="abs footnav" style="left:459px">About us</div>
<div class="abs footnav" style="left:506px">Merchants</div>
<div class="abs footnav" style="left:554px">Signup</div>
<div class="abs footnav" style="left:593px">Blog</div>
<div class="abs footnav" style="left:625px">Contact us</div>
<div class="abs footnav" style="left:672px">Stay With us</div>
<div class="abs" style="left:725px;top:950px;display:flex;gap:3px">
  <span style="width:11px;height:11px;background:#3b5998"></span>
  <span style="width:11px;height:11px;background:#d8412f"></span>
  <span style="width:11px;height:11px;background:#4fb6e8"></span>
</div>
<div class="abs bottombar">
  <span class="abs" style="left:202px;top:3px">© 2014 bluvendmarket - All Rights Reserved</span>
  <span class="abs" style="left:377px;top:3px"><a href="#">Terms &amp; Conditions</a> &nbsp;|&nbsp; <a href="#">Privacy Statement</a></span>
</div>

</body>
</html>
```